Brisk Orchard Website Design

About The Client:
Brisk Orchard is a sugar-free foods chain store providing services to Diabetics. They focus on the China domestic market. They describe themselves as being the 3rd space for Diabetics, the space between hospital and the home that help improve the quality of life for people wit Diabetes (see attached infographics).

They regularly hold education and advice events throughout the China. Brisk Orchard distribute a wide product range of food that is suitable for diabetic people. Brisk Orchard operate as a Franchise, providing business development services and Industry knowledge. They are actively seeking business partnerships at present.

The Brief:
Design a Home page and secondary information page(PSD only no code) that communicates our company services and company philosophy(3rd Space).
The final design should communicate 'Health, Social Responsibility and Professionalism'.
Colour scheme should orientate around Blue and White, see attached logo.

Websites we like:

http://lumo.vextrand.com/home/

https://www.corvapay.com/

http://gate.zv.com/

Hello all, the client has advised us that he want to display the professional advice service available for diabetic people more so than a food distributor. The client is also hoping to use his website as a marketing platform to attract affiliates and build partnerships as part of Brisk Orchard's business expansion strategy.

So can you make the page more corporate, reliable and professional. Use images of experts/doctors interacting with patients and also training/knowledge transfer images.

Thanks

Hello all, could you include stock images of both Chinese and Caucasians

Yeaahhh, Infographics and photos have been uploaded. Feel free to use them in your designs and also as references.

Target Market(s)

The target market is Chinese B2B in the Diabetics industry and Entrepreneurs looking to cooperate with Brisk Orchard.

Industry/Entity Type

Education

Requirements
Must have
• menu navigation with 7-8 sections,
a full screen background image,
Social Media icons,
Logo in top left,
Site search.
Nice to have
• The website must be clear and easy to use, less complicated.

See attached files of some Brisk Orchard infographics. Feel free to include elements of these into the design.
Should not have
• Should not use stock images of people from any other country, the client wants stock images of Chinese people only. Avoid photos showing obesity.

```html
<!DOCTYPE html>
<html lang="en">
<head>
<meta charset="utf-8">
<title>Brisk Orchard</title>
<link rel="stylesheet" href="https://fonts.googleapis.com/css2?family=Bree+Serif&family=Didact+Gothic&family=Roboto:wght@400;700&display=swap">
<style>
:root{
  --navy:#0b4a7c;
  --sky:#0aa0e8;
  --sky-light:#4fc3f7;
  --red:#e8212b;
  --ink:#333;
  --muted:#6b6b6b;
  --band:#f1f1f1;
  --line:#d6d6d6;
  --name:#1a8fd6;
}
*{box-sizing:border-box;margin:0;padding:0}
html,body{width:1094px;height:1200px;overflow:hidden}
body{position:relative;background:#fff;font-family:"Roboto",Arial,sans-serif;color:var(--ink)}
.abs{position:absolute}

/* top bar */
.topbar{left:0;top:0;width:1094px;height:42px;background:var(--navy)}
.search{left:360px;top:8px;width:158px;height:25px;background:#fff;border-radius:13px;font-size:10px;color:#999;padding:6px 0 0 14px}
.search svg{position:absolute;right:12px;top:8px}
.callout{right:242px;top:13px;font-size:10.5px;font-weight:700;color:#fff;white-space:nowrap;line-height:15px}
.callout .hl{color:var(--sky-light)}
.callout .phone{font-size:14px;margin-left:3px}
.divider{left:862px;top:10px;width:1px;height:22px;background:#3a6f99}
.social{top:12px;width:18px;height:18px;background:var(--sky)}
.social.round{border-radius:50%}

/* header */
.brand{left:139px;top:62px;display:flex;align-items:center;gap:8px;font-family:"Bree Serif",Georgia,serif;font-size:17px;color:var(--sky)}
.brand i{display:block;width:22px;height:22px;background:var(--sky)}
.nav a{position:absolute;top:81px;font-family:"Bree Serif",Georgia,serif;font-size:12.5px;color:var(--ink);text-decoration:none;white-space:nowrap}
.nav .home{left:365px;top:76px;width:79px;height:28px;border:1px solid #ccc;border-radius:14px;color:var(--red);text-align:center;padding-top:5px}

/* hero */
.hero{left:0;top:139px;width:1094px;height:391px;background:linear-gradient(90deg,#0a96dc,#12a9ef 50%,#0a9de4)}
.hero-title{left:0;width:1118px;top:270px;text-align:center;font-family:"Didact Gothic",sans-serif;font-size:40px;line-height:48px;color:#fff;letter-spacing:.3px;font-weight:400}
.hero-sub{left:0;width:1144px;top:320px;text-align:center;font-family:Georgia,"Times New Roman",serif;font-size:16px;color:#fff}
.hero-btn{left:462px;top:379px;width:168px;height:28px;border:2px solid #fff;border-radius:14px;color:#fff;font-size:11.5px;text-align:center;padding-top:6px}
.arrow{top:314px}

/* band */
.band{left:0;top:530px;width:1094px;height:368px;background:var(--band);border-bottom:1px solid #e2e2e2}
.col-title{font-family:"Bree Serif",Georgia,serif;font-weight:400;font-size:21px;line-height:24px;color:var(--ink)}
.col-title span{display:block;font-size:17.5px;color:var(--muted)}
.event-date{font-size:9px;font-weight:700;color:#444}
.event-text{width:172px;font-size:10.3px;line-height:12.5px;color:#333}
.pill{width:115px;height:29px;border:2px solid #ddd;border-radius:15px;background:#fff;font-family:"Bree Serif",Georgia,serif;font-size:10px;color:#555;text-align:center;padding-top:7px}
.quote-mark{font-family:Georgia,serif;font-weight:700;font-size:40px;color:#999;line-height:1}
.quote-text{width:150px;font-size:8.8px;line-height:11px;color:#444}
.quote-name{font-size:12px;font-weight:700;color:var(--name)}

/* feature card */
.card{left:378px;top:441px;width:338px;height:401px;background:#fff;border:1px solid var(--line)}
.card-title{left:0;width:336px;top:16px;text-align:center;font-family:"Bree Serif",Georgia,serif;font-weight:400;font-size:27px;line-height:30px;color:var(--ink)}
.card-title span{display:block;font-size:21px;color:var(--muted)}
.card-photo{left:5px;top:99px;width:327px;height:133px;background:linear-gradient(135deg,#e8e2d8,#b8a99a 45%,#5e6a82)}
.card-lead{left:20px;width:296px;top:249px;text-align:center;font-size:10px;line-height:13px;font-weight:700;color:#222}
.card-text{left:14px;width:308px;top:294px;text-align:center;font-size:10.3px;line-height:12.5px;color:#444}
.card-btn{left:84px;top:349px;width:166px;height:27px;border-radius:14px;background:var(--red);color:#fff;font-family:"Bree Serif",Georgia,serif;font-size:10px;text-align:center;padding-top:7px}

/* products */
.section-title{left:124px;top:916px;font-family:"Bree Serif",Georgia,serif;font-weight:400;font-size:21px;color:var(--ink)}
.product{top:968px;width:111px}
.product .thumb{width:111px;height:111px;border:1px solid var(--line);padding:3px;background:#fff}
.product .thumb div{width:103px;height:103px;background:linear-gradient(160deg,#a9c46a,#7ea54a 60%,#b9cf8a)}
.product p{margin-top:7px;text-align:center;font-family:"Bree Serif",Georgia,serif;font-size:10px;color:#555}

/* footer */
.footer{left:0;top:1150px;width:1094px;height:50px;background:var(--navy);color:#fff;font-size:10.5px;text-align:center;padding-top:20px}
</style>
</head>
<body>

<header>
  <div class="abs topbar"></div>
  <div class="abs search">Search here...
    <svg width="9" height="9" viewBox="0 0 10 10"><circle cx="4" cy="4" r="3" fill="none" stroke="#888" stroke-width="1.4"/><line x1="6.2" y1="6.2" x2="9" y2="9" stroke="#888" stroke-width="1.4"/></svg>
  </div>
  <div class="abs callout">For Knowledgeable advice - <span class="hl">Please call us :</span> <span class="phone">1-800-555-0142</span></div>
  <div class="abs divider"></div>
  <div class="abs social round" style="left:884px"></div>
  <div class="abs social" style="left:911px"></div>
  <div class="abs social" style="left:938px"></div>

  <div class="abs brand"><i></i>Brisk Orchard</div>
  <nav class="nav">
    <a class="home" href="#">Home</a>
    <a href="#" style="left:479px">About us</a>
    <a href="#" style="left:584px">Professional Advice</a>
    <a href="#" style="left:757px">Our Products</a>
    <a href="#" style="left:891px">Testimonials</a>
  </nav>
</header>

<section>
  <div class="abs hero" role="img" aria-label="Blue-tinted photo of a doctor advising patients"></div>
  <h1 class="abs hero-title">HEALTHY IS FOR EVERYONE</h1>
  <p class="abs hero-sub">Better Sugar free foods for a naturally better life.</p>
  <div class="abs hero-btn">PROFESSIONAL ADVICE</div>
  <svg class="abs arrow" style="left:135px" width="48" height="48" viewBox="0 0 48 48"><circle cx="24" cy="24" r="22.5" fill="none" stroke="#fff" stroke-width="2"/><polyline points="27,18 21,24 27,30" fill="none" stroke="#fff" stroke-width="2.4"/></svg>
  <svg class="abs arrow" style="left:909px" width="48" height="48" viewBox="0 0 48 48"><circle cx="24" cy="24" r="22.5" fill="none" stroke="#fff" stroke-width="2"/><polyline points="21,18 27,24 21,30" fill="none" stroke="#fff" stroke-width="2.4"/></svg>
</section>

<section>
  <div class="abs band"></div>

  <h2 class="abs col-title" style="left:130px;top:551px">Education and<span>Advice events</span></h2>

  <svg class="abs" style="left:130px;top:619px" width="27" height="27" viewBox="0 0 27 27"><rect x="0" y="3" width="27" height="24" fill="#8a8a8a"/><rect x="5" y="0" width="3" height="6" fill="#8a8a8a"/><rect x="19" y="0" width="3" height="6" fill="#8a8a8a"/><g fill="#f1f1f1"><rect x="4" y="11" width="4" height="4"/><rect x="11" y="11" width="4" height="4"/><rect x="18" y="11" width="4" height="4"/><rect x="4" y="18" width="4" height="4"/><rect x="11" y="18" width="4" height="4"/><rect x="18" y="18" width="4" height="4"/></g></svg>
  <div class="abs event-date" style="left:129px;top:652px">Sep 23</div>
  <p class="abs event-text" style="left:175px;top:620px">Lorem ipsum dolor sit amet adipiscing elit, sed diam nonummy nibh euismod tincidunt ut laoreet dolore magna aliquam erat volutpat.</p>

  <svg class="abs" style="left:130px;top:709px" width="27" height="27" viewBox="0 0 27 27"><rect x="0" y="3" width="27" height="24" fill="#8a8a8a"/><rect x="5" y="0" width="3" height="6" fill="#8a8a8a"/><rect x="19" y="0" width="3" height="6" fill="#8a8a8a"/><g fill="#f1f1f1"><rect x="4" y="11" width="4" height="4"/><rect x="11" y="11" width="4" height="4"/><rect x="18" y="11" width="4" height="4"/><rect x="4" y="18" width="4" height="4"/><rect x="11" y="18" width="4" height="4"/><rect x="18" y="18" width="4" height="4"/></g></svg>
  <div class="abs event-date" style="left:129px;top:742px">Sep 23</div>
  <p class="abs event-text" style="left:175px;top:708px">Lorem ipsum dolor sitconsectetuer</p>
  <p class="abs event-text" style="left:175px;top:732px">adipiscing elit, sed diam nonummy nibh euismod tincidunt ut laoreet dolore magna aliquam erat volutpat.</p>

  <div class="abs pill" style="left:178px;top:804px">MORE EVENTS</div>

  <article class="abs card">
    <h2 class="abs card-title">Healthy Food Choices<span>for diabetic patient</span></h2>
    <div class="abs card-photo" role="img" aria-label="Photo of staff advising customers at a table in a sugar-free food store"></div>
    <p class="abs card-lead">Brisk Orchard distribute a wide product range of food that is suitable for diabetic people</p>
    <p class="abs card-text">Lorem ipsum dolor sit amet, consectetuer adipiscing elit, sed diam nonummy nibh euismod tincidunt ut laoreet dolore magna aliquam erat volutpat. Ut wisi enim ad minim veniam,</p>
    <div class="abs card-btn">KNOW MORE ABOUT US</div>
  </article>

  <h2 class="abs col-title" style="left:748px;top:551px">What People<span>Say about us!</span></h2>

  <div class="abs quote-mark" style="left:745px;top:616px">&ldquo;</div>
  <p class="abs quote-text" style="left:772px;top:637px">Ut wisi enim ad minim veniam, quis nostrud exerci tation ullamcorper suscipit lobortis nisl ut aliquip ex ea commodo consequat.</p>
  <div class="abs quote-name" style="left:772px;top:684px">Martin Keller - China</div>
  <div class="abs quote-mark" style="left:924px;top:678px">&rdquo;</div>

  <div class="abs quote-mark" style="left:745px;top:704px">&ldquo;</div>
  <p class="abs quote-text" style="left:772px;top:725px">Ut wisi enim ad minim veniam, quis nostrud exerci tation ullamcorper suscipit lobortis nisl ut aliquip ex ea commodo consequat.</p>
  <div class="abs quote-name" style="left:772px;top:772px">Ravi Mehta - Sangai</div>
  <div class="abs quote-mark" style="left:924px;top:766px">&rdquo;</div>

  <div class="abs pill" style="left:787px;top:804px">MORE EVENTS</div>
</section>

<section>
  <h2 class="abs section-title">Top Selling Products</h2>
  <div class="abs product" style="left:168px"><div class="thumb"><div role="img" aria-label="Product photo: fresh salad plate"></div></div><p>DUIS AUTEM</p></div>
  <div class="abs product" style="left:326px"><div class="thumb"><div role="img" aria-label="Product photo: fresh salad plate"></div></div><p>DUIS AUTEM</p></div>
  <div class="abs product" style="left:483px"><div class="thumb"><div role="img" aria-label="Product photo: fresh salad plate"></div></div><p>DUIS AUTEM</p></div>
  <div class="abs product" style="left:640px"><div class="thumb"><div role="img" aria-label="Product photo: fresh salad plate"></div></div><p>DUIS AUTEM</p></div>
  <div class="abs product" style="left:797px"><div class="thumb"><div role="img" aria-label="Product photo: fresh salad plate"></div></div><p>DUIS AUTEM</p></div>
</section>

<footer class="abs footer">&copy; 2013 briskorchard.com, All Rights Reserved</footer>

</body>
</html>
```